Business Cards/Stationary/Letterhead for Crestline Weight Loss Center
Be Healthy, Be Fit, and Be Ready to Lose Weight!
Creative Brief
Simple
Derek Tolsan, PA
Physician Assistant, Co-founder
52816 Birchwood Lane Fremont, CA 94592-7731
CrestlineSlim@mailhaven.example
www.crestlineslim.example
Aim for Results with Crestline Weight Loss! HCG, Appetite Suppressants,B12/B-Complex injections, Menu Plans, Exercise Plans, Nutriceuticals, Supplements.
Present this card to a friend; If your friend signs up, you will receive a 20% discount. The referrals are endless. If you refer 5 friends who sign up then you will receive 100% discount on your next visit. Just make sure your friend puts your name down in the "referral" section of the information sheet and you will be that much closer to saving. (Discount will only apply to weight loss program, discount only applicable for one month or week supply of medication. Non-transferrable. Referral cannot be an existing patient.) Appointment Date: _________ Time: _____

```html
<!DOCTYPE html>
<html lang="en">
<head>
<meta charset="utf-8">
<title>Crestline Weight Loss Center – Stationery</title>
<link href="https://fonts.googleapis.com/css2?family=Open+Sans:wght@400;600;700&display=swap" rel="stylesheet">
<style>
  :root{
    --bg:#c8a57a;
    --paper:#ffffff;
    --paper-shade:#f3f3f3;
    --green:#8cbb2b;
    --orange:#e5771d;
    --ink:#6b6b6b;
    --faint:#eef3e3;
    --label:#4a3a28;
    --shadow:rgba(60,40,20,.35);
  }
  *{margin:0;padding:0;box-sizing:border-box}
  html,body{width:1200px;height:446px;overflow:hidden}
  body{background:var(--bg);font-family:"Open Sans",Arial,sans-serif;position:relative}
  .piece{position:absolute;background:var(--paper);box-shadow:0 2px 6px var(--shadow);overflow:hidden}
  .label{position:absolute;font-size:6px;letter-spacing:.5px;color:var(--label);text-transform:uppercase;text-align:center;white-space:nowrap}
  .section-title{position:absolute;left:10px;top:190px;font-size:7px;letter-spacing:.6px;color:var(--label);text-transform:uppercase}
  .brand{display:flex;align-items:center;gap:3px;position:absolute;color:var(--green);font-weight:600;white-space:nowrap}
  .brand .dot{border-radius:50%;background:var(--green);flex:none}
  .wave{position:absolute;left:0;bottom:0;width:100%}
  .tiny{position:absolute;font-size:3.6px;line-height:5px;color:var(--ink);white-space:nowrap}
  .footer-line{position:absolute;left:0;right:0;text-align:center;font-size:3.6px;color:#fff}
  .watermark{position:absolute;border-radius:50%;background:var(--faint)}

  /* business cards */
  .card-front{left:10px;top:211px;width:129px;height:40px}
  .card-front .brand{left:6px;top:8px;font-size:6px}
  .card-front .brand .dot{width:9px;height:9px}
  .card-back{left:10px;top:283px;width:129px;height:60px}
  .card-back .copy{position:absolute;left:7px;right:7px;top:7px;font-size:3.4px;line-height:4.8px;color:var(--green)}

  /* letterheads */
  .letterhead{top:17px;width:274px;height:391px}
  .lh-one{left:170px}
  .lh-two{left:475px}
  .letterhead .brand{left:50px;top:20px;font-size:7px}
  .letterhead .brand .dot{width:12px;height:12px}
  .letterhead .contact{left:178px;top:20px;color:var(--green)}
  .letterhead .watermark{left:82px;top:110px;width:110px;height:150px}

  /* envelope backs */
  .env-back-green{left:842px;top:32px;width:308px;height:58px}
  .env-back-green svg,.env-back-orange svg{position:absolute;left:0;top:0;width:100%;height:100%}
  .env-back-orange{left:818px;top:96px;width:332px;height:142px}
  .env-back-orange .brand{left:158px;top:104px;font-size:0}
  .env-back-orange .brand .dot{width:16px;height:16px}

  /* envelope front */
  .env-front{left:800px;top:252px;width:350px;height:150px}
  .env-front .brand{left:12px;top:12px;font-size:6.5px}
  .env-front .brand .dot{width:11px;height:11px}
</style>
</head>
<body>

<div class="section-title">Stationery Elements</div>

<!-- Business card front -->
<div class="piece card-front">
  <div class="brand"><span class="dot"></span>Crestline Weight Loss Center</div>
  <div class="tiny" style="left:70px;top:20px">Derek Tolsan, PA<br>Physician Assistant, Co-founder</div>
  <svg class="wave" viewBox="0 0 129 10" preserveAspectRatio="none" height="10">
    <path d="M0 4 C40 0 80 9 129 2 L129 10 L0 10Z" fill="var(--orange)"/>
    <path d="M0 6 C45 3 85 10 129 5 L129 10 L0 10Z" fill="var(--green)"/>
  </svg>
</div>
<div class="label" style="left:10px;top:256px;width:129px">Business Card Front</div>

<!-- Business card back -->
<div class="piece card-back">
  <div class="copy">Present this card to a friend; if your friend signs up, you will receive a 20% discount. Refer 5 friends and your next visit is free.<br>Appointment Date: ________ Time: _____</div>
</div>
<div class="label" style="left:10px;top:362px;width:129px">Business Card Back</div>

<!-- Letterhead option 1 -->
<div class="piece letterhead lh-one">
  <div class="brand"><span class="dot"></span>Crestline Weight Loss Center</div>
  <div class="tiny contact">52816 Birchwood Lane Fremont, CA 94592-7731<br>CrestlineSlim@mailhaven.example<br>www.crestlineslim.example</div>
  <div class="watermark" role="img" aria-label="Faint brand emblem decoration"></div>
  <svg class="wave" viewBox="0 0 274 40" preserveAspectRatio="none" height="40">
    <path d="M0 14 C90 -2 180 34 274 6 L274 40 L0 40Z" fill="var(--orange)"/>
    <path d="M0 22 C100 8 180 40 274 16 L274 40 L0 40Z" fill="var(--green)"/>
  </svg>
  <div class="footer-line" style="bottom:6px">Aim for Results with Crestline Weight Loss!</div>
</div>
<div class="label" style="left:170px;top:420px;width:274px">Letterhead Option 1</div>

<!-- Letterhead option 2 -->
<div class="piece letterhead lh-two">
  <div class="brand"><span class="dot"></span>Crestline Weight Loss Center</div>
  <div class="tiny contact">52816 Birchwood Lane Fremont, CA 94592-7731<br>CrestlineSlim@mailhaven.example<br>www.crestlineslim.example</div>
  <div class="watermark" role="img" aria-label="Faint brand emblem decoration"></div>
  <svg class="wave" viewBox="0 0 274 40" preserveAspectRatio="none" height="40">
    <path d="M0 14 C90 -2 180 34 274 6 L274 40 L0 40Z" fill="var(--orange)"/>
    <path d="M0 22 C100 8 180 40 274 16 L274 40 L0 40Z" fill="var(--green)"/>
  </svg>
  <div class="footer-line" style="bottom:6px">www.crestlineslim.example</div>
</div>
<div class="label" style="left:475px;top:420px;width:274px">Letterhead Option 2</div>

<!-- Envelope back, green flap -->
<div class="piece env-back-green">
  <svg viewBox="0 0 308 58" preserveAspectRatio="none">
    <path d="M0 0 H308 V44 Q154 62 0 44Z" fill="var(--green)"/>
  </svg>
</div>

<!-- Envelope back, orange flap -->
<div class="piece env-back-orange">
  <svg viewBox="0 0 332 142" preserveAspectRatio="none">
    <rect x="0" y="60" width="332" height="82" fill="var(--paper-shade)"/>
    <path d="M0 0 H332 V44 Q166 74 0 44Z" fill="var(--orange)"/>
  </svg>
  <div class="brand"><span class="dot"></span></div>
</div>

<!-- Envelope front -->
<div class="piece env-front">
  <div class="brand"><span class="dot"></span>Crestline Weight Loss Center</div>
  <div class="tiny" style="left:26px;top:25px">52816 Birchwood Lane Fremont, CA 94592-7731</div>
  <svg class="wave" viewBox="0 0 350 30" preserveAspectRatio="none" height="30">
    <path d="M0 12 C110 -2 220 28 350 6 L350 30 L0 30Z" fill="var(--orange)"/>
    <path d="M0 18 C120 6 220 32 350 13 L350 30 L0 30Z" fill="var(--green)"/>
  </svg>
</div>
<div class="label" style="left:800px;top:420px;width:350px">Envelope Option 1</div>

</body>
</html>
```